Velvet & Bloom Hair Extensions needs a business card

We need a business card designed for an online luxury hair extensions business called Velvet & Bloom, we already have a logo and need an innovative business card (2-sided preferably). The strap line for the brand is 'Luxury Hair At Every Touchpoint!'. The brand is a premium brand selling virgin hair extensions and the target market is the mid-affluent ethnic woman as such the design should reflect this. The brand logo is grey and can be sent when requested.

Target Market(s)

25 to 35 year mid-affluent ethnic woman (Afro-American, Mixed Race, Asian)

Industry/Entity Type

Hair

Colors

Designer to choose colors to be used in the design.

Requirements
Must have
• Business Name: Velvet and Bloom
Strapline: Luxury hair at every touchpoint!
Domain: ​www.velvetandbloom-demo.com
Email: info@velvetandbloom-demo.com
sales and enquiries
44 07391 xxxxxxx

Please use the grey main brand logo depicted in page 2 of the attached pdf document

```html
<!DOCTYPE html>
<html lang="en">
<head>
<meta charset="utf-8">
<title>Velvet &amp; Bloom – Business Card</title>
<link rel="stylesheet" href="https://fonts.googleapis.com/css2?family=Nunito:wght@800&family=Questrial&display=swap">
<style>
  :root {
    --backdrop: #3b7f98;
    --card-white: #ffffff;
    --card-shade: #e4e4e4;
    --gold: #cd9334;
    --gold-deep: #b27d2e;
    --brand-grey: #8e8e8e;
    --hair-grey: #a9a9a9;
    --contact-teal: #3e9c8c;
    --text-light: #ffffff;
  }
  * { margin: 0; padding: 0; box-sizing: border-box; }
  html, body {
    width: 1200px;
    height: 1200px;
    overflow: hidden;
    background: var(--backdrop);
  }
  .sheet {
    position: relative;
    width: 1200px;
    height: 1200px;
  }
  .card {
    position: absolute;
    top: 263px;
    width: 374px;
    height: 674px;
    overflow: hidden;
    background: radial-gradient(ellipse at 55% 40%, var(--card-white) 55%, var(--card-shade) 100%);
  }
  .card--front { left: 170px; }
  .card--back { left: 656px; }
  .card__band {
    position: absolute;
    inset: 0;
    width: 100%;
    height: 100%;
  }
  .hair-artwork {
    position: absolute;
    left: 0;
    top: 0;
    width: 228px;
    height: 238px;
    background: radial-gradient(ellipse at 35% 45%, var(--hair-grey) 0%, #c4c4c4 60%, rgba(255,255,255,0) 100%);
  }
  .brand-name {
    position: absolute;
    left: 22px;
    top: 250px;
    font-family: "Questrial", sans-serif;
    font-size: 31px;
    letter-spacing: 1px;
    color: var(--brand-grey);
    white-space: nowrap;
  }
  .strapline {
    position: absolute;
    left: 0;
    width: 100%;
    top: 478px;
    text-align: center;
    font-family: "Nunito", sans-serif;
    font-weight: 800;
    font-size: 21px;
    line-height: 26px;
    color: var(--text-light);
  }
  .web-address {
    position: absolute;
    left: 0;
    width: 100%;
    top: 132px;
    text-align: center;
    font-family: "Questrial", sans-serif;
    font-size: 23px;
    color: var(--text-light);
  }
  .contact {
    position: absolute;
    left: 0;
    width: 100%;
    text-align: center;
    font-family: "Questrial", sans-serif;
    font-size: 19px;
    line-height: 30px;
    color: var(--contact-teal);
  }
  .contact--phone { top: 476px; }
  .contact--email { top: 601px; }
</style>
</head>
<body>
<main class="sheet">
  <section class="card card--front" aria-label="Business card front">
    <svg class="card__band" viewBox="0 0 374 674" preserveAspectRatio="none" aria-hidden="true">
      <defs>
        <radialGradient id="gold-front" cx="0.5" cy="0.55" r="0.75">
          <stop offset="0.45" stop-color="var(--gold)"/>
          <stop offset="1" stop-color="var(--gold-deep)"/>
        </radialGradient>
      </defs>
      <polygon points="0,442 374,264 374,674 0,674" fill="url(#gold-front)"/>
    </svg>
    <div class="hair-artwork" role="img" aria-label="Grey brand illustration of flowing hair"></div>
    <div class="brand-name">Velvet &amp; Bloom</div>
    <p class="strapline">Luxury hair at every<br>touchpoint!</p>
  </section>

  <section class="card card--back" aria-label="Business card back">
    <svg class="card__band" viewBox="0 0 374 674" preserveAspectRatio="none" aria-hidden="true">
      <defs>
        <radialGradient id="gold-back" cx="0.5" cy="0.35" r="0.75">
          <stop offset="0.45" stop-color="var(--gold)"/>
          <stop offset="1" stop-color="var(--gold-deep)"/>
        </radialGradient>
      </defs>
      <polygon points="0,0 374,0 374,231 0,401" fill="url(#gold-back)"/>
    </svg>
    <p class="web-address">www.velvetandbloom-demo.com</p>
    <p class="contact contact--phone">sales and enquiries<br>44 07391 xxxxxxx</p>
    <p class="contact contact--email">info@velvetandbloom-demo.com</p>
  </section>
</main>
</body>
</html>
```